Business card design needed

I need a business card that sets my business apart from big gyms and intimidating personal trainers. My personal training business focuses on outdoor and client in-home training, in an environment that is both enjoyable and sustainable for the client.
I train males and females, however a large proportion of my clientelle are female, so I would like the card to lean towards females, but still have a bit of masculine appeal about it.
My business colours are a deep sky blue and lightish red/orange (as seen in logo)

Contact Information for Business Card

Your Wellbeing & Motion Guide
Discover a happier, healthier you!
Benedict Harlow- Health and Fitness Professional
Locations all across the Yarra Valley and Eastern Suburbs of Melbourne
0498315260
benedictharlowpt@quillmail.com.au

Requirements
Must have
• - Mobile number must stand out
- The 'Locations all across the Yarra Valley and Eastern Suburbs of Melbourne' must be clear and easy to read (different colour maybe?)

```html
<!DOCTYPE html>
<html lang="en">
<head>
<meta charset="utf-8">
<title>Business Card – Benedict Harlow</title>
<link href="https://fonts.googleapis.com/css2?family=Quicksand:wght@400;700&family=Roboto:ital,wght@1,700&family=Roboto+Mono:wght@400&display=swap" rel="stylesheet">
<style>
  :root {
    --page: #ffffff;
    --card: #ffffff;
    --sky-blue: #1a75bb;
    --coral: #e9522a;
    --orange-deep: #f07027;
    --orange-light: #f4921f;
    --orange-stripe: #f39a1e;
    --ink-dark: #3b3b3b;
    --ink-light: #ffffff;
    --phone-ink: #eeeeee;
  }
  * { box-sizing: border-box; margin: 0; padding: 0; }
  html, body {
    width: 1200px; height: 1000px; overflow: hidden;
    background: var(--page);
  }
  .card {
    position: absolute; left: 135px; top: 222px;
    width: 917px; height: 498px;
    background: var(--card); overflow: hidden;
    font-family: "Quicksand", sans-serif;
  }
  .card__band { position: absolute; left: 0; top: 0; width: 917px; height: 498px; }
  .brand-mark {
    position: absolute; left: 80px; top: 45px;
    width: 192px; height: 192px; border-radius: 50%;
    background: var(--coral);
  }
  .brand-name {
    position: absolute; left: 300px; top: 78px; width: 560px;
    font-weight: 700; font-size: 44px; line-height: 50px;
    color: var(--sky-blue); text-align: center;
  }
  .tagline {
    position: absolute; left: 296px; top: 170px;
    font-family: "Roboto", sans-serif; font-style: italic; font-weight: 700;
    font-size: 34px; color: var(--coral); letter-spacing: 0.3px;
  }
  .contact { position: absolute; font-size: 21px; font-weight: 400; color: var(--ink-light); white-space: nowrap; }
  .contact--email { right: 8px; top: 344px; font-size: 20px; }
  .contact--name { left: 10px; top: 373px; }
  .contact--area { left: 13px; top: 402px; color: var(--ink-dark); }
  .contact--slogan { left: 10px; top: 431px; }
  .contact--phone { right: 10px; top: 460px; font-size: 25px; }
  .contact--phone .phone-number { font-family: "Roboto Mono", monospace; font-size: 20px; color: var(--phone-ink); }
</style>
</head>
<body>
  <div class="card">
    <svg class="card__band" viewBox="0 0 917 498" aria-hidden="true">
      <defs>
        <linearGradient id="bandFill" x1="0" y1="0" x2="1" y2="0">
          <stop offset="0" stop-color="var(--orange-deep)"/>
          <stop offset="0.5" stop-color="var(--orange-light)"/>
          <stop offset="1" stop-color="var(--orange-deep)"/>
        </linearGradient>
      </defs>
      <path d="M0 279 Q 470 350 917 270 L917 498 L0 498 Z" fill="var(--orange-stripe)"/>
      <path d="M0 293 Q 470 364 917 283 L917 498 L0 498 Z" fill="url(#bandFill)"/>
    </svg>

    <div class="brand-mark"></div>
    <div class="brand-name">Your Wellbeing &amp; Motion Guide</div>
    <div class="tagline">Discover a happier, healthier you!</div>

    <div class="contact contact--email">benedictharlowpt@quillmail.com.au</div>
    <div class="contact contact--name">Benedict Harlow - Health and Fitness Professional</div>
    <div class="contact contact--area">Locations all across the Yarra Valley and Eastern Suburbs of Melbourne</div>
    <div class="contact contact--slogan">Your Wellbeing &amp; Motion Guide Discover a happier, healthier you!</div>
    <div class="contact contact--phone">Telephone: <span class="phone-number">0498315260</span></div>
  </div>
</body>
</html>
```